Flyer Design Project

We need a flyer (in Spanish) for:
"Feria Cántaro & Telar Brisa Alta 2013"
This event will be held in Los Angeles CA and would like to attract exhibitors.
Must include the information provided in the word file.
Updates

Target Market(s)

Tequila producers and distributors

Industry/Entity Type

Event

Requirements
Must have
• pictures to be used at your discretion

```html
<!DOCTYPE html>
<html lang="es">
<head>
<meta charset="utf-8">
<title>Feria Cántaro & Telar Brisa Alta 2013</title>
<link href="https://fonts.googleapis.com/css2?family=Montserrat:wght@600&family=Arimo:ital,wght@0,400;0,700;1,700&display=swap" rel="stylesheet">
<style>
  :root {
    --page-bg: #e9e6e1;
    --paper: #ffffff;
    --ink: #2a2a2a;
    --brand-red: #b3191f;
    --brand-green: #4aa43b;
    --dark-top: #4a0d0d;
    --dark-bottom: #0c0c0c;
  }
  * { margin: 0; padding: 0; box-sizing: border-box; }
  html, body { width: 1200px; height: 1000px; overflow: hidden; background: var(--page-bg); }
  .flyer {
    position: absolute; left: 250px; top: 0;
    width: 700px; height: 1000px;
    background: var(--paper); overflow: hidden;
    font-family: "Arimo", Arial, sans-serif; color: var(--ink);
  }
  .flyer-art { position: absolute; inset: 0; }
  .event-name {
    position: absolute; left: 44px; top: 92px; width: 430px;
    font-family: "Montserrat", Arial, sans-serif; font-weight: 600;
    line-height: 1.05;
  }
  .event-name .lead { display: block; font-size: 50px; letter-spacing: -1px; color: var(--brand-red); }
  .event-name .rest { display: block; font-size: 24px; margin-top: 6px; color: var(--ink); }
  .event-name .city { display: block; font-size: 24px; color: var(--brand-red); }
  .tagline {
    position: absolute; left: 40px; top: 234px; width: 460px;
    font-weight: 700; font-style: italic; font-size: 14px; line-height: 1.3; text-align: center;
  }
  .body-copy {
    position: absolute; left: 40px; top: 290px; width: 410px;
    font-size: 12.2px; line-height: 1.3;
  }
  .body-copy p { margin-bottom: 11px; }
  .contacts { margin-top: 16px; font-weight: 700; font-size: 12.2px; line-height: 1.32; }
  .contacts .block { margin-bottom: 14px; }
  .website {
    position: absolute; left: 70px; top: 900px;
    font-weight: 700; font-style: italic; font-size: 14px;
  }
</style>
</head>
<body>
<main class="flyer">
  <svg class="flyer-art" width="700" height="1000" viewBox="0 0 700 1000">
    <defs>
      <linearGradient id="darkPanel" x1="0" y1="0" x2="0" y2="1">
        <stop offset="0" stop-color="#4a0d0d"/>
        <stop offset="0.45" stop-color="#2a0707"/>
        <stop offset="1" stop-color="#0c0c0c"/>
      </linearGradient>
      <linearGradient id="cityTone" x1="0" y1="0" x2="0" y2="1">
        <stop offset="0" stop-color="#5a0b0b"/>
        <stop offset="0.6" stop-color="#9a1d10"/>
        <stop offset="1" stop-color="#d4621d"/>
      </linearGradient>
      <linearGradient id="agaveTone" x1="0" y1="0" x2="1" y2="1">
        <stop offset="0" stop-color="#9fb0a6" stop-opacity="0.25"/>
        <stop offset="1" stop-color="#5d6d63" stop-opacity="0.45"/>
      </linearGradient>
      <radialGradient id="toneTasting" cx="0.5" cy="0.5" r="0.6">
        <stop offset="0" stop-color="#c9c2b6"/><stop offset="1" stop-color="#5b5148"/>
      </radialGradient>
      <radialGradient id="toneJars" cx="0.5" cy="0.5" r="0.6">
        <stop offset="0" stop-color="#e9a64b"/><stop offset="1" stop-color="#8d4319"/>
      </radialGradient>
      <radialGradient id="toneToast" cx="0.5" cy="0.5" r="0.6">
        <stop offset="0" stop-color="#c58f6c"/><stop offset="1" stop-color="#4a3026"/>
      </radialGradient>
    </defs>

    <rect class="dark-panel" width="700" height="1000" fill="url(#darkPanel)"/>
    <g role="img" aria-label="Fotografía nocturna de rascacielos iluminados frente al agua">
      <rect x="420" y="0" width="280" height="500" fill="url(#cityTone)" opacity="0.85"/>
    </g>

    <path class="red-band" d="M0 1000 L0 930 C320 880 560 700 610 470 L700 470 L700 1000 Z" fill="var(--brand-red)"/>
    <path class="dark-edge" d="M0 1000 L0 975 C330 930 600 720 650 470 L700 470 L700 1000 Z" fill="var(--dark-bottom)"/>

    <path class="paper-area" d="M0 0 L300 0 C560 70 640 360 585 560 C520 770 300 900 0 955 Z" fill="var(--paper)"/>
    <g role="img" aria-label="Fotografía tenue de un campo de agave con un jimador">
      <path d="M0 260 L430 260 C520 420 560 560 520 660 C450 800 260 900 0 950 Z" fill="url(#agaveTone)"/>
    </g>
    <path class="green-arc" d="M300 0 C560 70 640 360 585 560 C520 770 300 900 0 955" fill="none" stroke="var(--brand-green)" stroke-width="9"/>
    <path class="red-arc" d="M0 968 C330 915 560 760 600 520" fill="none" stroke="var(--brand-red)" stroke-width="7"/>

    <g role="img" aria-label="Fotografía circular de catadores revisando barricas de tequila">
      <circle cx="580" cy="517" r="70" fill="url(#toneTasting)" stroke="#fff" stroke-width="3"/>
    </g>
    <g role="img" aria-label="Fotografía circular de cántaros de barro decorados">
      <circle cx="585" cy="715" r="122" fill="url(#toneJars)" stroke="#fff" stroke-width="3"/>
    </g>
    <g role="img" aria-label="Fotografía circular de amigos brindando con caballitos de tequila">
      <circle cx="496" cy="878" r="95" fill="url(#toneToast)" stroke="#fff" stroke-width="3"/>
    </g>
  </svg>

  <h1 class="event-name">
    <span class="lead">Feria Cántaro</span>
    <span class="rest">&amp; Telar Brisa Alta 2013</span>
    <span class="city">Los Angeles</span>
  </h1>

  <p class="tagline">¡Vinculando marcas emergentes e innovadoras en una época de descubrimiento de sabores mundiales!</p>

  <section class="body-copy">
    <p>Chile, España, Escocia, Francia, Argentina, Polonia, Mexico – cuando buscamos que beber, buscamos en el mundo, y ese mundo termina en nuestros vasos. Queremos lo mejor, lo más sabroso, lo interesante y estamos dispuestos a recorrer grandes distancias para obtenerlo.</p>
    <p>La promoción y la creatividad son, quizás, aún más importante en tiempos de incertidumbre económica, cuando se es implacable en la búsqueda de nuevos clientes. Con unas perspectivas más amplias, más globales, ya sea sondeando tradiciones centenarias, o la exploración de las fronteras de las bebidas de moda, buscando nuevas mercados, o re-inventando su marca para mantenerse competitivos.</p>
    <p>En esta edición especializada en Tequila, vamos a discutir las técnicas, procesos creativos, perfiles de sabor, tecnologías, y los ingredientes que son cada vez más esenciales de la caja de herramientas del Coctelero (Mixologist) del siglo 21.</p>
    <p>Tendremos una competencia de las cuatro variedades de tequila: Blanco, Reposado, Añejo y Extra Añejo; con reconocimiento a los ganadores de cada categoría.</p>
    <p>Acompáñanos, los días 29 y 30 de agosto 2013, donde se vincularan, consumidores, bares, detallistas, restaurantes y distribuidores, en la matriz de creatividad coctelera, talento culinario, sabores de moda y uno de los mercados más importantes e influyentes del mundo.</p>
    <p>&nbsp;&nbsp;&nbsp;Para oportunidades de patrocinio y exhibición:</p>
    <div class="contacts">
      <div class="block">(USA)<br>Ramiro T. Olvera – Director<br>Tel. + 818-555-0147<br>rolvera@brisaltaferia.com</div>
      <div class="block">(Mexico)<br>Ing. Julián E. Paredes<br>Tel. 333-555-0192<br>jparedes@brisaltaferia.com</div>
    </div>
  </section>

  <p class="website">www.brisaltaferia.com</p>
</main>
</body>
</html>
```